PLUM BUSINESS CARD

Need a business card and logo. The company name is PLUM (Coastal Society of Junior Equestrian Arts). It's a business that offers horseback riding lessons to young girls. Please put my name: Marlene Tobbitt and a place for email and phone number. I would like the card to look feminine and soft. I like script type lettering. I want the card to be white or ivory with black or gray and hot pink print. A horse head outline would be cool, something whimsical. Think teen girl who likes glamour. Also, I give western riding lessons. So I like faded out background Images of western saddles, cowgirls, horses with long hair, ropes, horses in sunset...mabe the word PLUM can be made out of a lasso rope?

Just updated my project with a little more detail

Target Market(s)

Young girls/ cowgirls, western riding

Industry/Entity Type

Horseback Riding

Font styles to use
Script

Colors
e34197

Requirements
Must have
• A logo of PLUM.
Must say Coastal Society of Junior Equestrian Arts
Colors are Pink and Black with an elegant, glamorous, feminine look.
Nice to have
• Could have a picture or outline of a horse

```html
<!DOCTYPE html>
<html lang="en">
<head>
<meta charset="utf-8">
<title>PLUM Business Card</title>
<link rel="stylesheet" href="https://fonts.googleapis.com/css2?family=Jost:wght@400;500&display=swap">
<style>
  :root {
    --pink: #e34197;
    --ink-gray: #6f6f6f;
    --soft-gray: #8a8a8a;
    --paper: #fbfbfa;
    --backdrop: #f2f2f2;
    --swirl: #e9e9e7;
    --white: #ffffff;
  }
  * { margin: 0; padding: 0; box-sizing: border-box; }
  html, body {
    width: 1200px; height: 1000px; overflow: hidden;
    background: radial-gradient(ellipse at 55% 40%, var(--white) 0%, var(--backdrop) 75%);
    font-family: "Jost", "Futura", sans-serif;
  }
  .canvas { position: relative; width: 1200px; height: 1000px; }

  /* Business card front */
  .card {
    position: absolute; left: 230px; top: 130px;
    width: 740px; height: 420px;
    background: var(--paper);
    box-shadow: 0 18px 40px rgba(0,0,0,0.12), 0 2px 6px rgba(0,0,0,0.08);
    overflow: hidden;
  }
  .card-backdrop-art {
    position: absolute; right: 0; top: 0; width: 470px; height: 372px;
    background: linear-gradient(160deg, rgba(233,233,231,0) 0%, var(--swirl) 45%, rgba(233,233,231,0.2) 100%);
  }
  .name-banner {
    position: absolute; left: 270px; top: 74px;
    background: var(--pink); color: var(--white);
    font-weight: 400; font-size: 40px; letter-spacing: 1px;
    padding: 4px 18px 2px; line-height: 1.1; text-transform: uppercase;
  }
  .job-title {
    position: absolute; left: 300px; top: 128px;
    color: var(--soft-gray); font-size: 17px; letter-spacing: 2px; text-transform: uppercase;
  }
  .card-brand { position: absolute; left: 26px; top: 214px; }
  .brand-name {
    color: var(--pink); font-weight: 500; font-size: 54px; letter-spacing: 4px; line-height: 1;
  }
  .brand-rule { height: 2px; width: 230px; background: var(--pink); margin: 8px 0 6px; }
  .brand-tagline { color: var(--ink-gray); font-size: 15px; line-height: 1.2; width: 240px; }
  .contact {
    position: absolute; right: 28px; bottom: 70px;
    color: var(--ink-gray); font-size: 13px; letter-spacing: 0.5px;
    display: grid; gap: 8px; justify-items: start;
  }
  .contact-row { display: flex; align-items: center; gap: 8px; }
  .contact-row svg { width: 12px; height: 12px; fill: var(--ink-gray); }
  .contact-gap { width: 20px; }
  .card-band {
    position: absolute; left: 0; bottom: 0; width: 100%; height: 16px; background: var(--pink);
  }

  /* Logo lockup */
  .logo-lockup { position: absolute; left: 46px; top: 830px; }
  .logo-lockup .brand-name { font-size: 60px; }
  .logo-lockup .brand-rule { width: 200px; }
  .logo-lockup .brand-tagline { font-size: 12px; width: 220px; }

  /* Presentation label */
  .sheet-label {
    position: absolute; left: 848px; top: 910px; width: 352px; height: 44px;
    background: var(--white); border: 1px solid #cfcfcf; border-right: none;
    display: flex; align-items: center; justify-content: center;
    font-size: 20px; letter-spacing: 1px; color: #222; text-transform: uppercase;
  }
</style>
</head>
<body>
<main class="canvas">
  <section class="card">
    <div class="card-backdrop-art" role="img" aria-label="Faint gray flowing decorative swirl pattern"></div>
    <h1 class="name-banner">Marlene Tobbitt</h1>
    <p class="job-title">Instructor</p>
    <div class="card-brand">
      <div class="brand-name">PLUM</div>
      <div class="brand-rule"></div>
      <p class="brand-tagline">Coastal Society of Junior Equestrian Arts</p>
    </div>
    <div class="contact">
      <div class="contact-row">
        <svg viewBox="0 0 12 12"><path d="M2 1h2l1 3-1.5 1a6 6 0 0 0 3.5 3.5L8 7l3 1v2a1 1 0 0 1-1 1A9 9 0 0 1 1 2a1 1 0 0 1 1-1z"/></svg>
        <span>+91 47 5820934</span>
        <span class="contact-gap"></span>
        <svg viewBox="0 0 12 12"><path d="M3 0h6a1 1 0 0 1 1 1v10a1 1 0 0 1-1 1H3a1 1 0 0 1-1-1V1a1 1 0 0 1 1-1zm0 1.5v7h6v-7zM5 10h2v1H5z"/></svg>
        <span>+91 62 9041573</span>
      </div>
      <div class="contact-row">
        <span>@</span>
        <span>marlenetobbitt@trailridelessons.com</span>
      </div>
    </div>
    <div class="card-band"></div>
  </section>

  <section class="logo-lockup">
    <div class="brand-name">PLUM</div>
    <div class="brand-rule"></div>
    <p class="brand-tagline">Coastal Society of Junior Equestrian Arts</p>
  </section>

  <div class="sheet-label">PLUM Business Card</div>
</main>
</body>
</html>
```